Jewellery retailer needs a flyer design please

We need a flyer to represent our business.

Our company provides The lowest priced diamonds in Australia.
We are wholesales who sell direct to the public
We GENUINELY are 50-70% cheaper than other retail stores.

We guarantee the lowest prices, even in the unlikely event a customer finds a cheaper price than ours, we will beat it too.

Well tell our customers if youre not buying from us then you're paying too much.

Please include website www.amberloomstore.com.au
and facebook page www.facebook.com/mosslightcove.

We have location in Harbourgate Parramatta, and Harbourgate Liverpool, NSW.

Im sorry, this is the first time ive done this, so i hope ive given the information you need.

Target Market(s)

People wanting to buy engagement rings are our biggest customers.

Industry/Entity Type

Retail

Colors
276db0
3276b5
86acd3
cedeed

Requirements
Must have
• Simple, to the point! We need people to know that we have the lowest prices without compromising on quality
Nice to have
• I am very very open to anything. I do not have any particular expectations

```html
<!DOCTYPE html>
<html lang="en">
<head>
<meta charset="utf-8">
<title>Amber Loom – Flyer</title>
<link href="https://fonts.googleapis.com/css2?family=Didact+Gothic&family=Mulish:wght@400;700&display=swap" rel="stylesheet">
<style>
  :root {
    --backdrop: #2f2f2f;
    --paper: #ffffff;
    --ink: #2b2b2b;
    --ink-soft: #444444;
    --brand-navy: #2a3f6a;
    --seal-light: #8a8a8a;
    --seal-dark: #555555;
    --photo-light: #f4f5f7;
    --photo-mid: #d6dae0;
  }
  * { margin: 0; padding: 0; box-sizing: border-box; }
  html, body { width: 1139px; height: 1200px; overflow: hidden; }
  body { background: var(--backdrop); position: relative; font-family: "Didact Gothic", "Century Gothic", sans-serif; color: var(--ink); }

  .flyer { position: absolute; left: 163px; top: 20px; width: 812px; height: 1160px; background: var(--paper); }

  .headline { position: absolute; left: 34px; top: 52px; width: 400px; font-size: 40px; font-weight: 400; line-height: 1.1; color: var(--ink); }

  .brand { position: absolute; left: 470px; top: 78px; width: 300px; display: flex; align-items: center; justify-content: center; gap: 14px; }
  .brand-dot { width: 20px; height: 20px; border-radius: 50%; background: var(--brand-navy); }
  .brand-name { font-size: 44px; color: var(--brand-navy); }

  .guarantee { position: absolute; left: 0; top: 232px; width: 812px; text-align: center; font-size: 23px; line-height: 1.35; color: var(--ink-soft); }

  .ring-photo { position: absolute; left: 70px; top: 330px; width: 660px; height: 390px; border-radius: 50%;
    background: radial-gradient(ellipse at 45% 35%, var(--photo-light) 0%, var(--photo-mid) 75%, #e8eaee 100%); }

  .claim { position: absolute; left: 420px; top: 740px; width: 370px; text-align: center; line-height: 1.2; color: var(--ink); }
  .claim .sm { font-size: 36px; display: block; }
  .claim .lg { font-size: 46px; display: block; }
  .claim .md { font-size: 40px; display: block; }

  .seal { position: absolute; top: 838px; width: 166px; height: 166px; border-radius: 50%;
    background: radial-gradient(circle at 40% 35%, var(--seal-light), var(--seal-dark));
    display: flex; align-items: center; justify-content: center; text-align: center;
    color: #fff; font-size: 20px; line-height: 1.15; padding: 0 34px; }
  .seal-lowest { left: 25px; }
  .seal-wholesale { left: 215px; padding: 0 26px; }

  .locations { position: absolute; left: 34px; top: 1052px; font-family: "Mulish", sans-serif; font-size: 21px; line-height: 1.4; color: var(--ink); }
  .locations h2 { font-size: 21px; font-weight: 700; }

  .web-links { position: absolute; right: 37px; top: 1076px; text-align: right; font-family: "Mulish", sans-serif; font-size: 18px; line-height: 1.6; color: var(--ink); }
</style>
</head>
<body>
  <main class="flyer">
    <h1 class="headline">If you're not buying from us then you're paying too much.</h1>

    <div class="brand">
      <span class="brand-dot"></span>
      <span class="brand-name">Amber Loom</span>
    </div>

    <p class="guarantee">We guarantee the lowest prices, even in the unlikely event<br>a customer finds a cheaper price than ours, we will beat it too.</p>

    <div class="ring-photo" role="img" aria-label="Photograph of a white gold solitaire engagement ring with a heart-shaped diamond"></div>

    <p class="claim">
      <span class="sm">We</span>
      <span class="lg">GENUINELY</span>
      <span class="sm">are</span>
      <span class="lg">50-70%</span>
      <span class="md">cheaper than</span>
      <span class="md">other retail stores</span>
    </p>

    <div class="seal seal-lowest">Lowest Priced Diamonds in Australia</div>
    <div class="seal seal-wholesale">Wholesalers who sell direct to the public</div>

    <div class="locations">
      <h2>Our Locations</h2>
      <p>Harbourgate Parramatta, NSW</p>
      <p>Harbourgate Liverpool, NSW</p>
    </div>

    <div class="web-links">
      <p>www.amberloomstore.com.au</p>
      <p>www.facebook.com/mosslightcove</p>
    </div>
  </main>
</body>
</html>
```